Income Tax Flyer - Updates Needed

Just need to update this flyer design and give it a new look. We would like to keep all the same wording but make it stand out a little more. Our selling point is the "Same Day Tax Advance up to $6,000"

Industry/Entity Type

Lending, Small Loans, Tax Services, Title Loans, Personal Loans

```html
<!DOCTYPE html>
<html lang="en">
<head>
<meta charset="utf-8">
<title>Same Day Tax Advance Flyer</title>
<link rel="stylesheet" href="https://fonts.googleapis.com/css2?family=Bebas+Neue&family=Jost:wght@300&family=Montserrat:wght@500;600;700;800&display=swap">
<style>
  :root {
    --board: #58595b;
    --board-label: #e4e4e6;
    --paper: #ffffff;
    --fade: #d3d4d6;
    --grey-light: #6d6e71;
    --grey-dark: #58595b;
    --red: #c1232a;
    --green: #124d2c;
    --green-text: #1a5a32;
    --rule: #d9d9db;
  }
  * { margin: 0; padding: 0; box-sizing: border-box; }
  html, body { width: 994px; height: 1200px; overflow: hidden; background: var(--board); }
  .board { position: relative; width: 994px; height: 1200px; background: var(--board); }
  .board-label {
    position: absolute; top: 60px; left: 0; width: 994px; text-align: center;
    font-family: "Jost", sans-serif; font-weight: 300; font-size: 44px; color: var(--board-label);
    letter-spacing: 1px;
  }
  .flyer {
    position: absolute; left: 161px; top: 153px; width: 673px; height: 953px;
    background: var(--paper); overflow: hidden;
    box-shadow: 0 0 30px rgba(0,0,0,.35);
  }
  .hero-fade {
    position: absolute; left: 0; top: 0; width: 673px; height: 490px;
    background: linear-gradient(180deg, #ffffff 0%, #ffffff 40%, var(--fade) 100%);
  }
  .headline { position: absolute; left: 38px; font-family: "Bebas Neue", sans-serif; line-height: 1; white-space: nowrap; }
  .headline-same { top: 19px; font-size: 106px; color: var(--grey-light); letter-spacing: -1px; }
  .headline-tax { top: 84px; font-size: 282px; color: var(--red); letter-spacing: -4px; }
  .headline-advance { top: 316px; font-size: 112px; color: var(--grey-dark); letter-spacing: -1px; }
  .headline-upto {
    position: absolute; left: 98px; top: 415px; font-family: "Montserrat", sans-serif;
    font-weight: 600; font-size: 64px; line-height: 1; color: var(--grey-dark); letter-spacing: -1px;
  }
  .hero-photo {
    position: absolute; left: 308px; top: 133px; width: 365px; height: 357px;
    background: radial-gradient(ellipse at 55% 45%, #f4f4f4 0%, #e6e6e6 55%, #d6d6d8 100%);
  }
  .brand {
    position: absolute; left: 414px; top: 50px; width: 169px; text-align: center;
    font-family: "Montserrat", sans-serif; font-weight: 700; font-size: 24px; line-height: 1.1;
    color: var(--green);
  }
  .amount-band { position: absolute; left: 0; top: 490px; width: 673px; height: 151px; background: var(--green); }
  .amount {
    position: absolute; left: 40px; top: 498px; font-family: "Bebas Neue", sans-serif;
    font-size: 150px; line-height: 1; color: #fff; letter-spacing: -3px;
  }
  .benefits {
    position: absolute; left: 391px; top: 529px; width: 240px;
    background: #fff; box-shadow: 0 8px 24px rgba(0,0,0,.12);
  }
  .benefit {
    height: 112px; display: flex; flex-direction: column; align-items: center; justify-content: flex-end;
    padding-bottom: 16px; border-top: 1px solid var(--rule);
  }
  .benefit:first-child { border-top: none; }
  .benefit svg { width: 52px; height: 52px; margin-bottom: 12px; }
  .benefit-label {
    font-family: "Montserrat", sans-serif; font-weight: 700; font-size: 12.5px; color: var(--grey-dark);
  }
  .pitch {
    position: absolute; left: 38px; top: 655px; font-family: "Bebas Neue", sans-serif;
    font-size: 57px; line-height: 48px; color: var(--grey-light); letter-spacing: -1px;
  }
  .pitch-accent { color: var(--green); }
  .contact-call {
    position: absolute; left: 39px; top: 820px; font-family: "Montserrat", sans-serif;
    font-weight: 800; font-size: 19px; color: var(--green-text);
  }
  .phone-pill {
    position: absolute; left: 39px; top: 848px; width: 202px; height: 34px; border-radius: 17px;
    background: var(--red); color: #fff; font-family: "Montserrat", sans-serif; font-weight: 700;
    font-size: 20px; line-height: 34px; text-align: center;
  }
  .location {
    position: absolute; top: 891px; font-family: "Montserrat", sans-serif; font-size: 12px;
    line-height: 15px; color: var(--grey-dark); font-weight: 500;
  }
  .location-name { color: var(--green-text); font-weight: 700; }
  .location svg { position: absolute; left: -14px; top: 2px; width: 8px; height: 10px; }
  .location-divider { position: absolute; top: 894px; width: 1px; height: 50px; background: var(--red); }
</style>
</head>
<body>
<div class="board">
  <div class="board-label">A4 Flyer Design-2</div>

  <div class="flyer">
    <div class="hero-fade"></div>
    <div class="hero-photo" role="img" aria-label="Smiling man in a white shirt pointing at the headline while holding a fan of cash"></div>

    <div class="brand">Keystone<br>Finance</div>

    <div class="headline headline-same">SAME DAY</div>
    <div class="headline headline-tax">TAX</div>
    <div class="headline headline-advance">ADVANCE</div>
    <div class="headline-upto">UP TO</div>

    <div class="amount-band"></div>
    <div class="amount">$6,000</div>

    <div class="benefits">
      <div class="benefit">
        <svg viewBox="0 0 52 52" fill="none" stroke="#124d2c" stroke-width="2.6" stroke-linecap="round">
          <path d="M26 3a23 23 0 1 1-20 12"/>
          <path d="M26 3v5M49 26h-5M26 49v-5M3 26h5"/>
          <path d="M8 31c2 4 5 6 8 7l2-3-3-3-2 1c-1-1-2-2-2-4l1-2-3-3z"/>
          <text x="26" y="31" font-family="Montserrat, sans-serif" font-size="14" font-weight="700" fill="#124d2c" stroke="none" text-anchor="middle">24</text>
        </svg>
        <div class="benefit-label">Available In 24 Hours or Less</div>
      </div>
      <div class="benefit">
        <svg viewBox="0 0 52 52" fill="none" stroke="#124d2c" stroke-width="2.6" stroke-linejoin="round" stroke-linecap="round">
          <circle cx="30" cy="15" r="12"/>
          <text x="30" y="20" font-family="Montserrat, sans-serif" font-size="13" font-weight="700" fill="#124d2c" stroke="none" text-anchor="middle">$</text>
          <rect x="3" y="36" width="7" height="12"/>
          <path d="M10 39h8l6 3h8M10 46h18l18-12c-2-3-5-3-8-1l-8 5"/>
        </svg>
        <div class="benefit-label">Choose Your Loan Amount</div>
      </div>
      <div class="benefit">
        <svg viewBox="0 0 52 52" fill="none" stroke="#124d2c" stroke-width="2.6" stroke-linejoin="round" stroke-linecap="round">
          <rect x="2" y="4" width="6" height="12"/>
          <path d="M8 6h8l6 6"/>
          <rect x="18" y="12" width="30" height="16" rx="1"/>
          <circle cx="33" cy="20" r="4"/>
          <rect x="44" y="36" width="6" height="12"/>
          <path d="M44 38h-20c-3 0-4 3-1 4l8 2M44 46H24l-10-6c-2-2 0-4 2-3"/>
        </svg>
        <div class="benefit-label">Quick and Easy</div>
      </div>
    </div>

    <div class="pitch">FILE YOUR TAXES<br>AND APPLY FOR AN<br><span class="pitch-accent">EASY ADVANCE!</span></div>

    <div class="contact-call">CONTACT US TODAT!</div>
    <div class="phone-pill">(555) 314-2087</div>

    <div class="location" style="left:55px">
      <svg viewBox="0 0 8 10"><path d="M4 10C1 6 0 5 0 4a4 4 0 0 1 8 0c0 1-1 2-4 6z" fill="#c1232a"/><circle cx="4" cy="4" r="1.4" fill="#fff"/></svg>
      <div class="location-name">Riverside – North Cedar</div>
      4820-2 N. Cedar Ave<br>Riverside, Texas 78612
    </div>
    <div class="location-divider" style="left:222px"></div>
    <div class="location" style="left:253px">
      <svg viewBox="0 0 8 10"><path d="M4 10C1 6 0 5 0 4a4 4 0 0 1 8 0c0 1-1 2-4 6z" fill="#c1232a"/><circle cx="4" cy="4" r="1.4" fill="#fff"/></svg>
      <div class="location-name">Millbrook</div>
      2210 W Oak St Ste #410 Millbrook,<br>TX 78190
    </div>
    <div class="location-divider" style="left:477px"></div>
    <div class="location" style="left:506px">
      <svg viewBox="0 0 8 10"><path d="M4 10C1 6 0 5 0 4a4 4 0 0 1 8 0c0 1-1 2-4 6z" fill="#c1232a"/><circle cx="4" cy="4" r="1.4" fill="#fff"/></svg>
      <div class="location-name">Harlow</div>
      3307 S. E L Parker St<br>#204
    </div>
  </div>
</div>
</body>
</html>
```